4' x 8' Construction Project Sign, think of a very large business card

We need project signs for our construction sites, the sign will be mounted along the road so cars driving by can quickly read. the sign should be able to be read as cars drive by doing highway speed.

Think like your making a large business card

I would like to include "NOW HIRING" Superintendents, Project Managers, Pipe Foremen, Pipe Layers, and Equipment Operators

Description of services we provide should include

Civil Construction Services
Land Clearing
Excavation
Underground Utilities
Environmental Maintenance

The 2 objectives is to market to future clients and to recruit new employees

The sign will be mounted on posts at the entrance of our construction projects

Low design quality

Target Market(s)

Construction and land developers

Industry/Entity Type

Construction Company

Font styles to use
Other font styles liked:
• Hypatia Sans Pro lite

Colors

Designer to choose colors to be used in the design.

Requirements
Must have
• Clean and easy to read
• Civil Construction Services
• Land Clearing
• Excavation
• Underground Utilities
• Road Construction

```html
<!DOCTYPE html>
<html lang="en">
<head>
<meta charset="utf-8">
<title>Harlow Brothers – Now Hiring Project Sign</title>
<link rel="stylesheet" href="https://fonts.googleapis.com/css2?family=Alegreya+Sans:wght@400&family=Cabin:wght@500;700&display=swap">
<style>
  :root {
    --brand-blue: #3a55a4;
    --slate: #5d5e60;
    --ink: #535459;
    --rule: #b9cbe4;
    --paper: #ffffff;
    --backdrop: #adaaab;
    --bubble-edge: #d9d9dc;
  }
  * { margin: 0; padding: 0; box-sizing: border-box; }
  html, body {
    width: 1200px; height: 840px; overflow: hidden;
    background: var(--backdrop);
  }
  .sign {
    position: absolute; left: 0; top: 45px;
    width: 1200px; height: 750px;
    background: var(--paper);
    overflow: hidden;
  }
  .sign-art { position: absolute; inset: 0; }
  .hiring-callout {
    position: absolute; left: 226px; top: 170px; width: 384px;
    text-align: center; color: var(--paper);
    font-family: "Cabin", sans-serif; font-weight: 700;
    font-size: 80px; line-height: 82px; letter-spacing: 1px;
    text-shadow: 3px 4px 5px rgba(20, 30, 70, .55);
  }
  .position-list {
    position: absolute; left: 668px; top: 98px; width: 452px;
    list-style: none;
    font-family: "Alegreya Sans", sans-serif; font-weight: 400;
    font-size: 52px; color: var(--ink);
  }
  .position-list li {
    height: 71.5px; line-height: 70px;
    border-bottom: 2px solid var(--rule);
    white-space: nowrap;
  }
  .company {
    position: absolute; left: 668px; top: 520px;
    display: flex; align-items: center; height: 106px;
  }
  .company-mark { width: 80px; height: 80px; background: var(--brand-blue); }
  .company-divider { width: 2px; height: 106px; background: var(--slate); margin: 0 14px 0 16px; }
  .company-name {
    font-family: "Cabin", sans-serif; font-weight: 500; color: var(--brand-blue);
    text-transform: uppercase;
  }
  .company-name .primary { display: block; font-size: 36px; line-height: 38px; letter-spacing: 1px; }
  .company-name .secondary { display: block; font-size: 22px; line-height: 28px; letter-spacing: 6px; }
  .services-band {
    position: absolute; left: 0; bottom: 0; width: 1200px; height: 90px;
    display: flex; list-style: none;
    font-family: "Cabin", sans-serif; font-weight: 500; font-size: 31px; color: var(--paper);
  }
  .services-band li { display: flex; align-items: center; justify-content: center; white-space: nowrap; }
  .services-band .is-blue { background: var(--brand-blue); }
  .services-band .is-slate { background: var(--slate); }
</style>
</head>
<body>
  <main class="sign">
    <svg class="sign-art" width="1200" height="750" viewBox="0 0 1200 750" aria-hidden="true">
      <defs>
        <radialGradient id="halftone-glow" cx="0.55" cy="0.5" r="0.6">
          <stop offset="0" stop-color="#e6e7ea"/>
          <stop offset="1" stop-color="#ffffff"/>
        </radialGradient>
      </defs>
      <rect x="0" y="60" width="420" height="470" fill="url(#halftone-glow)"/>
      <circle cx="422" cy="276" r="192" fill="var(--bubble-edge)"/>
      <circle cx="418" cy="270" r="192" fill="var(--brand-blue)"/>
      <path d="M240 310 L205 342 L262 330 Z" fill="var(--brand-blue)"/>
    </svg>

    <svg style="position:absolute;left:0;top:290px" width="210" height="210" role="img" aria-label="Illustration of a hand holding a blue and grey megaphone">
      <defs>
        <linearGradient id="megaphone-tone" x1="0" y1="1" x2="1" y2="0">
          <stop offset="0" stop-color="#4a4b4f"/>
          <stop offset="1" stop-color="#4fb0e2"/>
        </linearGradient>
      </defs>
      <rect width="210" height="210" fill="url(#megaphone-tone)" opacity=".85"/>
    </svg>

    <h1 class="hiring-callout">NOW<br>HIRING!</h1>

    <ul class="position-list">
      <li>Superintendents</li>
      <li>Project Managers</li>
      <li>Pipe Foremen</li>
      <li>Pipe Layers</li>
      <li>Equipment Operators</li>
    </ul>

    <div class="company">
      <div class="company-mark"></div>
      <div class="company-divider"></div>
      <p class="company-name">
        <span class="primary">Harlow Brothers</span>
        <span class="secondary">Civil Construction</span>
      </p>
    </div>

    <ul class="services-band">
      <li class="is-blue" style="width:416px">Civil Construction Services</li>
      <li class="is-slate" style="width:236px">Land Clearing</li>
      <li class="is-blue" style="width:193px">Excavation</li>
      <li class="is-slate" style="width:355px">Underground Utilities</li>
    </ul>
  </main>
</body>
</html>
```